Landing Page für selbstständigen DJ
Zielgruppe
Ich bin ein selbstständiger DJ, spiele auf Hochzeiten, Pool-Party's, Geburtstagen, Familienfeiern und in Clubs.
Genres sind EDM, Techno, House, und 90er Hits.
Zielgruppe sind private Interessenten und Eigentümer von Clubs und Veranstalter
Aufgabenstellung
Einfaches Design, ans Logo angelehnt, clean
Gerne in Figma oder Adobe XD

```html
<!DOCTYPE html>
<html lang="de">
<head>
<meta charset="utf-8">
<title>Nico Varell – DJ Landingpage</title>
<link href="https://fonts.googleapis.com/css2?family=Oswald:wght@400;600;700&family=Open+Sans:wght@400;600&display=swap" rel="stylesheet">
<style>
:root{
  --plum:#561536;
  --maroon:#5c0f33;
  --magenta:#b3124f;
  --violet:#3b1b5e;
  --lime:#9dbb2c;
  --ghost:#eeeeee;
  --ink:#2a2a2a;
  --white:#ffffff;
}
*{margin:0;padding:0;box-sizing:border-box}
html,body{width:841px;height:1200px;overflow:hidden}
body{background:var(--plum);position:relative;font-family:"Open Sans",sans-serif;color:var(--ink)}
.page{position:absolute;left:270px;top:23px;width:300px;height:1153px;background:var(--white);overflow:hidden}
.abs{position:absolute}
.display{font-family:"Oswald",sans-serif;font-weight:700;text-transform:uppercase}

/* hero */
.hero{left:0;top:0;width:300px;height:182px;background:linear-gradient(120deg,var(--magenta) 0%,#7a1450 45%,var(--violet) 100%)}
.hero-photo{left:0;top:0;width:300px;height:182px}
.brand{left:7px;top:6px;color:var(--white);font-family:"Oswald",sans-serif;font-weight:700;font-size:6px;letter-spacing:.3px;line-height:1}
.nav{right:8px;top:8px;display:flex;gap:7px;font-family:"Oswald",sans-serif;font-weight:600;font-size:3px;color:var(--white);text-transform:uppercase}
.hero-title{left:60px;width:200px;top:58px;text-align:center;color:var(--white);font-size:24px;line-height:.98}
.hero-sub{left:60px;width:200px;top:109px;text-align:center;color:var(--white);font-size:6px}
.hero-btns{left:0;width:300px;top:122px;display:flex;justify-content:center;gap:5px;padding-left:10px}
.btn{font-family:"Oswald",sans-serif;font-weight:600;font-size:3px;text-transform:uppercase;padding:2px 3px;line-height:1}
.btn-lime{background:var(--lime);color:var(--ink)}
.btn-dark{background:var(--maroon);color:var(--white)}
.arrow{width:6px;height:6px;background:#111;display:flex;align-items:center;justify-content:center}
.arrow svg{width:4px;height:4px}

/* about */
.about-photo{left:57px;top:199px;width:93px;height:93px;background:linear-gradient(135deg,#bfe3ee,#8fcfe0)}
.about-text{left:163px;top:221px;width:90px}
.h-section{font-size:10px;color:var(--maroon);line-height:1}
.copy{font-size:2.6px;line-height:1.45;margin-top:3px}
.ticks{list-style:none;margin-top:3px;font-size:2.6px;line-height:2.6}
.ticks li::before{content:"";display:inline-block;width:2px;height:2px;background:var(--lime);margin-right:3px}

/* ghost titles */
.ghost{color:var(--ghost);font-size:29px;line-height:1;white-space:nowrap}

/* cards */
.card{position:absolute}
.card-img{width:88px;height:56px}
.card-title{font-family:"Oswald",sans-serif;font-weight:700;font-size:3.6px;color:var(--maroon);text-transform:uppercase;margin-top:3px;line-height:1}
.card-copy{font-size:2.5px;line-height:1.45;margin-top:1px;width:88px}

/* strip */
.strip{left:0;top:508px;width:300px;height:75px;display:flex}
.strip div{flex:1}

/* feedback */
.quote{left:57px;top:613px;width:187px;height:81px;background:var(--lime);text-align:center;padding:0 16px}
.quote-title{font-size:8.5px;line-height:1;color:var(--white);margin-top:13px}
.quote-copy{font-size:2.6px;line-height:1.45;margin-top:5px}
.quote-by{font-size:1.8px;margin-top:9px;color:#3a4a10}

/* request */
.req-title{left:57px;top:1039px;width:90px;font-size:8.5px;line-height:1;color:var(--maroon)}
.req-copy{left:57px;top:1068px;width:85px;font-size:2.6px;line-height:1.45}
.form{left:163px;top:1040px;width:81px}
.field{border-bottom:.4px solid #555;font-size:1.8px;line-height:1;padding-bottom:1px;margin-bottom:8px}
.row{display:flex;gap:4px}
.row .field{flex:1}
.check{font-size:1.8px;display:flex;align-items:center;gap:2px;margin-top:-3px}
.check span{width:2.5px;height:2.5px;border:.3px solid #555;display:inline-block}

/* footer */
.footer{left:0;top:1102px;width:300px;height:51px;background:var(--maroon);color:var(--white);text-align:center}
.foot-brand{font-family:"Oswald",sans-serif;font-weight:700;font-size:6px;margin-top:8px}
.foot-icons{display:flex;justify-content:center;gap:7px;margin-top:4px}
.foot-icons i{width:3.5px;height:3.5px;border:.4px solid var(--white);border-radius:50%}
.foot-line{width:74px;height:.4px;background:rgba(255,255,255,.4);margin:4px auto 3px}
.foot-small{font-size:1.8px;line-height:2.4}
</style>
</head>
<body>
<main class="page">

  <section class="abs hero">
    <div class="abs hero-photo" role="img" aria-label="Neonbeleuchtete Kopfhörer vor Magenta-Violett"></div>
    <div class="abs brand">NICO VARELL</div>
    <nav class="abs nav"><span>Start</span><span>Über mich</span><span>Musik</span><span>Feedback</span><span>Gigs</span><span>Kontakt</span></nav>
    <h1 class="abs display hero-title">Sound für<br>deine Nacht.</h1>
    <p class="abs hero-sub">Energie für deine Crowd</p>
    <div class="abs hero-btns"><span class="btn btn-lime">Jetzt anfragen »</span><span class="btn btn-lime">Hörprobe ansehen »</span></div>
    <div class="abs arrow" style="left:5px;top:90px"><svg viewBox="0 0 4 4"><path d="M2.6.6 1.2 2l1.4 1.4" fill="none" stroke="#fff" stroke-width=".5"/></svg></div>
    <div class="abs arrow" style="left:289px;top:90px"><svg viewBox="0 0 4 4"><path d="M1.4.6 2.8 2 1.4 3.4" fill="none" stroke="#fff" stroke-width=".5"/></svg></div>
  </section>

  <section>
    <div class="abs about-photo" role="img" aria-label="Weiße Kopfhörer und Sonnenbrille auf hellblauem Grund"></div>
    <div class="abs about-text">
      <h2 class="display h-section">Über mich</h2>
      <p class="copy">Ich bin Nico Varell, DJ aus XXX – spezialisiert auf Clubnächte, Hochzeiten &amp; private Events. Ich liebe energiegeladene Sets, Sound mit Herz und tanzbare Übergänge.</p>
      <ul class="ticks">
        <li>Club- &amp; Event-Erfahrung seit XXX Jahren</li>
        <li>Eigene Technik &amp; Licht möglich</li>
        <li>Musik tailored to audience</li>
      </ul>
    </div>
  </section>

  <section>
    <div class="abs display ghost" style="left:14px;top:307px">Musik &amp; Genres</div>
    <div class="card" style="left:57px;top:326px">
      <div class="card-img" style="background:linear-gradient(135deg,#1fb8bf,#0a8f98)" role="img" aria-label="Türkisfarbene Kopfhörer"></div>
      <div class="card-title">EDM</div><div class="card-copy">kraftvoll &amp; episch</div>
    </div>
    <div class="card" style="left:155px;top:326px">
      <div class="card-img" style="background:linear-gradient(135deg,#3a2fb0,#1a1030)" role="img" aria-label="Kopfhörer in Rot und Blau auf Schwarz"></div>
      <div class="card-title">Techno</div><div class="card-copy">düster &amp; hypnotisch</div>
    </div>
    <div class="card" style="left:57px;top:403px">
      <div class="card-img" style="background:linear-gradient(135deg,#336e78,#2a5c66)" role="img" aria-label="Rote Lautsprecherbox auf Petrol"></div>
      <div class="card-title">House</div><div class="card-copy">funky &amp; groovy</div>
    </div>
    <div class="card" style="left:155px;top:403px">
      <div class="card-img" style="background:linear-gradient(135deg,#8fd0ee,#5fb8e8)" role="img" aria-label="Kassetten und CDs auf Hellblau"></div>
      <div class="card-title">90er</div><div class="card-copy">Party-Classics &amp; Nostalgie</div>
    </div>
    <div class="abs btn btn-dark" style="left:127px;top:483px">Alle Hörproben ansehen »</div>
  </section>

  <div class="abs strip" role="img" aria-label="Fotoreihe: DJ-Pult, Mischpult und Plattenspieler in Neonlicht">
    <div style="background:linear-gradient(#6a3aa8,#3a2a7a);flex:.5"></div>
    <div style="background:linear-gradient(#5b2fb0,#c0602a)"></div>
    <div style="background:linear-gradient(#7a4ab8,#3a3a8a)"></div>
    <div style="background:linear-gradient(#3a3a3a,#5a5a5a)"></div>
    <div style="background:linear-gradient(#2a1a4a,#b02070);flex:.5"></div>
  </div>

  <section>
    <div class="abs display ghost" style="left:11px;top:599px">Feedback</div>
    <div class="abs quote">
      <p class="display quote-title">Er hat unsere Hochzeit gerockt –<br>kein Gast saß still!</p>
      <p class="quote-copy">Wir hatten eine absolut unvergessliche Party – von der romantischen Trauung bis zur letzten Tanzrunde um 4 Uhr früh. Danke für deinen perfekten Musikmix!</p>
      <p class="quote-by">Lea &amp; Tom R., Hochzeit im Mai</p>
    </div>
    <div class="abs arrow" style="left:61px;top:650px"><svg viewBox="0 0 4 4"><path d="M2.6.6 1.2 2l1.4 1.4" fill="none" stroke="#fff" stroke-width=".5"/></svg></div>
    <div class="abs arrow" style="left:230px;top:650px"><svg viewBox="0 0 4 4"><path d="M1.4.6 2.8 2 1.4 3.4" fill="none" stroke="#fff" stroke-width=".5"/></svg></div>
  </section>

  <section>
    <div class="abs display ghost" style="left:98px;top:712px">Events / Gigs</div>
    <div class="card" style="left:57px;top:735px">
      <div class="card-img" style="background:linear-gradient(90deg,#a6d8ec,#efb2c6)" role="img" aria-label="Kopfhörer mit roten Herzen"></div>
      <div class="card-title">Hochzeiten</div><div class="card-copy">Euer großer Tag verdient den perfekten Sound. Ich sorge für emotionale Begleitung beim Dinner – und eine volle Tanzfläche bis spät in die Nacht.</div>
    </div>
    <div class="card" style="left:155px;top:735px">
      <div class="card-img" style="background:linear-gradient(135deg,#f2bccb,#e7a6ba)" role="img" aria-label="Schallplatte mit Konfetti auf Rosa"></div>
      <div class="card-title">Geburtstage</div><div class="card-copy">Von 18 bis 80 – ich bringe den passenden Mix für jede Generation. Eure Lieblingssongs treffen auf Club-Vibes für die richtige Party-Stimmung.</div>
    </div>
    <div class="card" style="left:57px;top:818px">
      <div class="card-img" style="background:linear-gradient(135deg,#dceef8,#b9dcef)" role="img" aria-label="Kopfhörer, Muscheln und Sonnenbrille"></div>
      <div class="card-title">Poolpartys</div><div class="card-copy">Duft nach Sommer, kühle Drinks und der perfekte Beat. Ob Daydrinking oder Sundowner – ich liefere den Soundtrack zum Abtauchen.</div>
    </div>
    <div class="card" style="left:155px;top:818px">
      <div class="card-img" style="background:linear-gradient(135deg,#d8d8d8,#bdbdbd)" role="img" aria-label="Laptop, Kopfhörer und Schallplatten auf Grau"></div>
      <div class="card-title">Firmenfeiern</div><div class="card-copy">Ob Jahresfeier, Teamevent oder Messe-Party – ich sorge für entspannte Lounge-Beats oder eskalierende Afterwork-Vibes.</div>
    </div>
    <div class="card" style="left:57px;top:902px">
      <div class="card-img" style="background:linear-gradient(135deg,#6a2ad0,#e02a9a)" role="img" aria-label="Kopfhörer und Schallplatte in Pink und Lila"></div>
      <div class="card-title">Clubs &amp; Bars</div><div class="card-copy">Techno. House. 90er. Bass. Energie. Ich spiele Sets, die nicht nur den Dancefloor, sondern auch den Vibe des Abends prägen.</div>
    </div>
  </section>

  <section>
    <div class="abs display ghost" style="left:146px;top:995px">Anfrage</div>
    <h2 class="abs display req-title">Sag mir, wann &amp;<br>wo – ich bring<br>den Sound.</h2>
    <p class="abs req-copy">Du planst ein Event und suchst den passenden DJ? Ob Hochzeit, Clubnacht oder private Party – ich bringe die Musik, die eure Nacht unvergesslich macht. Schreib mir einfach, was du vorhast – ich melde mich schnellstmöglich zurück!</p>
    <form class="abs form">
      <div class="row"><div class="field">Vor- und Nachname</div><div class="field">E-Mail-Adresse</div></div>
      <div class="field">Eventdatum, Art und Ort / Location (z. B. Hochzeit, Geburtstag, Clubnacht)</div>
      <div class="field">Nachricht</div>
      <div class="check"><span></span>Ich stimme der Verarbeitung meiner Daten gemäß Datenschutz zu.</div>
      <div class="btn btn-dark" style="display:inline-block;margin-top:3px">Senden »</div>
    </form>
  </section>

  <footer class="abs footer">
    <div class="foot-brand">NICO VARELL</div>
    <div class="foot-icons"><i></i><i></i><i></i></div>
    <div class="foot-line"></div>
    <div class="foot-small">Impressum · Datenschutzerklärung</div>
    <div class="foot-small">© 2025 Nico Varell · All rights reserved</div>
  </footer>

</main>
</body>
</html>
```